Brivora Collective Business Card Design

We need a business card design for Brivora Collective. We are a healthcare recruiting, wellness and education company. We partner with medical facilities to find quality candidates. We also offer free wellness courses.
The final design should communicate an emphasis on recruiting and wellness
The main purpose of the business card is to utilized it for networking events, give to hospitals, executives, VCs surgery centers and clinics. I want it to be sleek, clean, use of our brand colors and professional.

```html
<!DOCTYPE html>
<html lang="en">
<head>
<meta charset="utf-8">
<title>Brivora Collective Business Card</title>
<link href="https://fonts.googleapis.com/css2?family=Montserrat:wght@400;700&family=Open+Sans:wght@400;600&display=swap" rel="stylesheet">
<style>
  :root {
    --page: #3a3a3a;
    --teal-deep: #035e57;
    --teal-ink: #02574f;
    --teal-bright: #00ab9d;
    --teal-soft: #0b7a70;
    --white: #ffffff;
  }
  html, body {
    margin: 0;
    width: 1200px;
    height: 875px;
    overflow: hidden;
    background: var(--page);
  }
  .canvas {
    position: relative;
    width: 1200px;
    height: 875px;
  }
  .card {
    position: absolute;
    top: 283px;
    width: 540px;
    height: 309px;
    border-radius: 18px;
    box-sizing: border-box;
    border-bottom: 3px solid var(--teal-bright);
    overflow: hidden;
  }
  .card-front {
    left: 40px;
    background: var(--white);
    display: flex;
    align-items: center;
    justify-content: center;
  }
  .brand {
    display: flex;
    flex-direction: column;
    align-items: flex-end;
  }
  .brand-square {
    width: 34px;
    height: 34px;
    background: var(--teal-ink);
    border-radius: 6px;
    align-self: center;
    margin-bottom: 16px;
  }
  .brand-name {
    font-family: "Montserrat", sans-serif;
    font-weight: 400;
    font-size: 44px;
    line-height: 1;
    color: var(--teal-ink);
    text-align: right;
  }
  .card-back {
    left: 620px;
    background: var(--teal-deep);
    color: var(--white);
  }
  .back-mark {
    position: absolute;
    left: 40px;
    top: 120px;
    width: 150px;
    height: 150px;
    border-radius: 22px;
    background: linear-gradient(135deg, var(--teal-bright), var(--teal-soft));
  }
  .back-info {
    position: absolute;
    top: 26px;
    right: 30px;
    text-align: right;
  }
  .back-brand {
    font-family: "Montserrat", sans-serif;
    font-weight: 400;
    font-size: 36px;
    line-height: 1;
    margin-bottom: 18px;
  }
  .person-name {
    font-family: "Montserrat", sans-serif;
    font-weight: 700;
    font-size: 22px;
    letter-spacing: 1px;
    margin: 0;
  }
  .person-role {
    font-family: "Open Sans", sans-serif;
    font-size: 13px;
    margin: 2px 0 12px;
  }
  .contact-list {
    list-style: none;
    margin: 0;
    padding: 0;
    font-family: "Open Sans", sans-serif;
    font-size: 12.5px;
    line-height: 1.7;
  }
  .contact-list li {
    display: flex;
    justify-content: flex-end;
    align-items: center;
    gap: 8px;
  }
  .contact-icon {
    width: 11px;
    height: 11px;
    fill: none;
    stroke: var(--white);
    stroke-width: 1.6;
  }
</style>
</head>
<body>
<main class="canvas">
  <section class="card card-front">
    <div class="brand">
      <span class="brand-square"></span>
      <span class="brand-name">Brivora<br>Collective</span>
    </div>
  </section>

  <section class="card card-back">
    <div class="back-mark" role="img" aria-label="Brand decoration area"></div>
    <div class="back-info">
      <div class="back-brand">Brivora<br>Collective</div>
      <h1 class="person-name">DANIEL REYES</h1>
      <p class="person-role">Founder &amp; CEO</p>
      <ul class="contact-list">
        <li>(555) 014-2290
          <svg class="contact-icon" viewBox="0 0 12 12"><path d="M2 1.5 L4 1.5 L5 4 L3.8 5 Q5 7.5 7 8.2 L8 7 L10.5 8 L10.5 10 Q6 10.5 3 7.5 Q1 5 2 1.5Z"/></svg>
        </li>
        <li>(555) 014-2291
          <svg class="contact-icon" viewBox="0 0 12 12"><rect x="3" y="1" width="6" height="10" rx="1"/></svg>
        </li>
        <li>(555) 014-2292
          <svg class="contact-icon" viewBox="0 0 12 12"><rect x="3" y="1" width="6" height="3"/><rect x="1" y="4" width="10" height="5" rx="1"/><rect x="3" y="8" width="6" height="3"/></svg>
        </li>
        <li>info@brivoracollective.com
          <svg class="contact-icon" viewBox="0 0 12 12"><rect x="1" y="2.5" width="10" height="7"/><path d="M1 2.5 L6 6.5 L11 2.5"/></svg>
        </li>
        <li>brivoracollective.com
          <svg class="contact-icon" viewBox="0 0 12 12"><circle cx="6" cy="6" r="5"/><path d="M1 6 H11 M6 1 Q3 6 6 11 Q9 6 6 1"/></svg>
        </li>
      </ul>
    </div>
  </section>
</main>
</body>
</html>
```